Bref créative
Stationery design for KORV Holdings
KORV Holdings - Motion Lessons & Media
Use same font as used in my logo
Trajan Bold
Bright & Fun-filled
Damian Whitcombe
IT & Technical Support
The Lumley House
12 Fenwick Lane
Ashcombe-Under-Lyne
Bristol
BS4 7QD
damian@korv.co
www.korv.co
This is the KORV Holdings logo.

```html
<!DOCTYPE html>
<html lang="en">
<head>
<meta charset="UTF-8">
<title>KORV Holdings – Business Card</title>
<link rel="stylesheet" href="https://fonts.googleapis.com/css2?family=Cinzel:wght@400;700&display=swap">
<style>
  :root {
    --gold-dark: #b8901c;
    --gold-mid: #d9b23a;
    --gold-light: #f3d872;
    --ink: #5a5346;
    --paper: #ffffff;
    --backdrop: #e4e4e4;
  }
  * { box-sizing: border-box; margin: 0; padding: 0; }
  html, body {
    width: 1200px; height: 984px; overflow: hidden;
    background: var(--backdrop);
    font-family: "Cinzel", serif;
  }
  .card {
    position: absolute; left: 200px;
    width: 800px; height: 457px;
    border-radius: 22px; overflow: hidden;
    box-shadow: 0 6px 18px rgba(0,0,0,0.12);
  }
  .card--back {
    top: 23px;
    background: linear-gradient(135deg, var(--gold-dark) 0%, var(--gold-light) 45%, var(--gold-mid) 70%, var(--gold-dark) 100%);
    display: flex; flex-direction: column; align-items: center; justify-content: center;
    color: var(--paper);
  }
  .back-name {
    font-weight: 700; font-size: 96px; letter-spacing: 4px; line-height: 1;
  }
  .back-web {
    margin-top: 18px; font-weight: 400; font-size: 16px; letter-spacing: 9px;
  }
  .card--front { top: 504px; background: var(--paper); }
  .front-name {
    position: absolute; top: 48px; width: 100%; text-align: center;
    font-weight: 700; font-size: 58px; color: var(--gold-mid); letter-spacing: 2px;
  }
  .person {
    position: absolute; top: 160px; right: 420px; text-align: right;
    color: var(--ink); font-size: 13px; line-height: 1.55;
  }
  .person__name { font-size: 21px; font-weight: 700; color: var(--gold-mid); margin-bottom: 2px; }
  .person__role { font-weight: 700; margin-bottom: 8px; }
  .contact {
    position: absolute; top: 166px; left: 420px; list-style: none;
    color: var(--ink); font-size: 13px; line-height: 1;
  }
  .contact li { display: flex; align-items: center; gap: 9px; height: 24px; }
  .contact__icon { width: 16px; height: 16px; flex: none; }
  .wave { position: absolute; left: 0; top: 0; width: 800px; height: 457px; }
</style>
</head>
<body>

<section class="card card--back">
  <div class="back-name">KORV</div>
  <div class="back-web">WWW.KORV.CO</div>
</section>

<section class="card card--front">
  <svg class="wave" viewBox="0 0 800 457" aria-hidden="true">
    <defs>
      <linearGradient id="band" x1="0" y1="0" x2="1" y2="1">
        <stop offset="0" stop-color="#b8901c"/>
        <stop offset="0.45" stop-color="#f3d872"/>
        <stop offset="1" stop-color="#c69e2a"/>
      </linearGradient>
    </defs>
    <path d="M0 365 C 220 300, 430 430, 800 335 L800 457 L0 457 Z" fill="url(#band)"/>
    <path d="M0 392 C 230 335, 450 448, 800 368" fill="none" stroke="#ffffff" stroke-width="7"/>
    <path d="M0 345 C 210 285, 440 405, 800 312" fill="none" stroke="url(#band)" stroke-width="2.5"/>
  </svg>

  <h1 class="front-name">KORV Holdings</h1>

  <address class="person" style="font-style:normal">
    <div class="person__name">Damian Whitcombe</div>
    <div class="person__role">IT &amp; Technical Support</div>
    <div>The Lumley House</div>
    <div>12 Fenwick Lane</div>
    <div>Ashcombe-Under-Lyne</div>
    <div>Bristol BS4 7QD</div>
  </address>

  <ul class="contact">
    <li><svg class="contact__icon" viewBox="0 0 16 16"><circle cx="8" cy="8" r="8" fill="#d9b23a"/><path d="M5 4.5l1.6-.3.8 2-1 .8a6 6 0 0 0 2.6 2.6l.8-1 2 .8-.3 1.6c-3.4.3-6.8-3.1-6.5-6.5z" fill="#fff"/></svg>0117 496 0321</li>
    <li><svg class="contact__icon" viewBox="0 0 16 16"><circle cx="8" cy="8" r="8" fill="#d9b23a"/><rect x="5.5" y="3.5" width="5" height="9" rx="1" fill="#fff"/></svg>07700 900 418</li>
    <li><svg class="contact__icon" viewBox="0 0 16 16"><circle cx="8" cy="8" r="8" fill="#d9b23a"/><rect x="4" y="5" width="8" height="6" fill="#fff"/></svg>0117 496 0322</li>
    <li><svg class="contact__icon" viewBox="0 0 16 16"><circle cx="8" cy="8" r="8" fill="#d9b23a"/><rect x="4" y="5" width="8" height="6" fill="#fff"/><path d="M4 5l4 3.2L12 5" fill="none" stroke="#d9b23a" stroke-width="1"/></svg>damian@korv.co</li>
    <li><svg class="contact__icon" viewBox="0 0 16 16"><circle cx="8" cy="8" r="8" fill="#d9b23a"/><circle cx="8" cy="8" r="4" fill="none" stroke="#fff" stroke-width="1.2"/><path d="M4 8h8M8 4v8" stroke="#fff" stroke-width="1"/></svg>www.korv.co</li>
  </ul>
</section>

</body>
</html>
```